Stationary for Wealth Management Firm

We need stationary design based on our new business cards. We would like it to be simple, clean and understated. A lot of our clients are seniors so the fonts cannot be too small. Our colors are dark blue and light grey.

This is what we need:

1. Letterhead US Letter – 8.5" x 11" CMYK 300 DPI
2. Invoice US Letter – 8.5" x 11" CMYK 300 DPI
3. Fax Cover Sheet US Letter – 8.5" x 11" CMYK 300 DPI
4. Email Signature

Including: logo, motto, address with phone and fax numbers, web address, and compliance disclosure.

5. Standard Envelope #10 – 9,5” x 4,125” CMYK 300 Dpi
6. Large Envelope – 9” x 12” CMYK 300 Dpi

Including: logo, motto, addresses without phone and fax numbers, web address, and compliance disclosure.

7. Letterhead Follower US Letter – 8.5" x 11" CMYK 300 DPI

Including: logo, motto, and web address.

8. Flat Invitation Cards – 6” x 4” CMYK 300 Dpi
9. Pocket Folder – 9" x 12”, CMYK 300 Dpi

Including: logo and motto.

Here is the info:

Company: Corlance Wealth Management LLC
Address 1: 4817 Hadley Ave. Suite K-12, Ashford Vale, PA, 19011
Phone 1: 1-215-555-0173
Address 2: 618 Marsh Circle, Penrow Twp., PA, 19360
Phone 2: 1-610-555-0146
Fax: 1-484-555-0192
Motto: A Legacy of Care (in grey #A8A8A8 and US Declaration font)
Web address: www.corlancewealth.example
Compliance disclosure: Securities and Advisory Services offered through QRT Financial. Member NEXOB/DAFT.

Industry/Entity Type

Business

Requirements
Must have
• Need to blend the business card look and feel with the brochure/website look and feel.

```html
<!DOCTYPE html>
<html lang="en">
<head>
<meta charset="utf-8">
<title>Corlance Wealth Management – Letterhead</title>
<link rel="stylesheet" href="https://fonts.googleapis.com/css2?family=Lato:wght@400;700&family=Montserrat:wght@400;700&family=Pinyon+Script&display=swap">
<style>
  :root{
    --navy:#1f3566;
    --badge:#3f67a0;
    --ink:#555a63;
    --grey:#a8a8a8;
    --paper:#f4f4f5;
    --backdrop:#e7e8ea;
    --rule:#2f4676;
  }
  *{margin:0;padding:0;box-sizing:border-box}
  html,body{width:1200px;height:800px;overflow:hidden;background:var(--backdrop)}
  .canvas{position:relative;width:1200px;height:800px;font-family:"Lato",sans-serif;color:var(--ink)}
  .badge{position:absolute;z-index:2;width:70px;height:62px}
  .badge text{font-family:"Montserrat",sans-serif;font-weight:700;font-size:26px;fill:var(--navy)}
  .sheet{position:absolute;z-index:1;top:82px;width:459px;height:646px;background:var(--paper);border:1px solid #dcdde0}
  .sheet--letter{left:90px}
  .sheet--follower{left:665px}
  .brand{position:absolute;left:35px;top:66px;display:flex;align-items:center;gap:7px}
  .brand__mark{width:14px;height:14px;background:var(--navy)}
  .brand__name{font-family:"Lato",sans-serif;font-weight:400;color:var(--navy);text-transform:uppercase;line-height:1.15}
  .brand__name span{display:block}
  .brand__line1{font-size:12.5px;letter-spacing:.6px}
  .brand__line2{font-size:6.6px;letter-spacing:.7px}
  .addresses{position:absolute;left:351px;top:19px;font-family:"Montserrat",sans-serif;font-size:4.6px;line-height:8.4px;color:#4a4f59;text-transform:uppercase;letter-spacing:.2px;white-space:nowrap}
  .addresses p+p{margin-top:4px}
  .addresses b{font-weight:700}
  .meta{position:absolute;left:60px;top:113px;font-family:"Montserrat",sans-serif;font-size:5.6px;line-height:9px;color:#3e434c}
  .meta b{font-weight:700}
  .letter-body{position:absolute;left:60px;top:138px;width:362px;font-size:6.1px;line-height:13px;color:var(--ink);text-align:justify}
  .letter-body p{margin-bottom:12px}
  .letter-body .salutation{margin-bottom:0}
  .signatory{position:absolute;left:60px;top:367px;font-family:"Montserrat",sans-serif;color:#3a3f48}
  .signatory__name{font-size:12.5px;line-height:13px}
  .signatory__name b{font-weight:700}
  .signatory__role{font-size:6.4px;color:#6a6f78}
  .signature{position:absolute;left:58px;top:402px;width:126px;height:66px;background:linear-gradient(135deg,#ececee,#e2e3e6);border-radius:2px}
  .footer{position:absolute;left:30px;top:598px;width:210px}
  .footer__motto{font-family:"Pinyon Script",cursive;font-size:9.5px;line-height:12px;color:var(--grey);margin-left:4px}
  .footer__rule{height:1px;background:var(--rule);margin:1px 0 3px}
  .footer__legal{font-family:"Montserrat",sans-serif;font-size:3.6px;line-height:5px;color:#4a4f59;text-transform:uppercase;white-space:nowrap}
  .footer__web{font-family:"Montserrat",sans-serif;font-weight:700;font-size:4.2px;line-height:6px;color:var(--navy);text-transform:uppercase}
</style>
</head>
<body>
<main class="canvas">

  <section class="sheet sheet--letter">
    <div class="brand">
      <div class="brand__mark"></div>
      <div class="brand__name"><span class="brand__line1">Corlance</span><span class="brand__line2">Wealth Management</span></div>
    </div>

    <div class="addresses">
      <p>4817 Hadley Ave. Suite K-12<br>Ashford Vale, PA, 19011<br><b>P.</b> 1-215-555-0173<br><b>F.</b> 1-484-555-0192</p>
      <p>618 Marsh Circle<br>Penrow Twp., PA, 19360<br><b>P.</b> 1-610-555-0146<br><b>F.</b> 1-484-555-0192</p>
    </div>

    <div class="meta">
      <p><b>Date :</b> Mon , 25 / 3 / 2013</p>
      <p><b>Recipient :</b> Mr.John Doe Sanderson</p>
    </div>

    <div class="letter-body">
      <p class="salutation">Dear Mr. Jhon Doe</p>
      <p>LoTrem ipsum dolor sit amet, consectetur adipiscing elit. Praesent vulputate, neque ac accumsan suscipit, justo turpis volutpat nisl, tempus fermentum eros tortor et elit. Vivamus porttitor faucibus gravida. Quisque pharetra gravida luctus. Donec eget turpis libero. Ut ac dolor urna, quis tempor nunc. Donec vitae mauris purus, euismod eleifend nulla. Lorem ipsum dolor sit amet, consectetur adipiscing elit. Donec ut purus tellus. Aenean quis dignissim lacus. Vestibulum suscipit vehicula cursus. Suspendisse potenti. Ut in sem nisi. Sed et massa leo.</p>
      <p>Fusce varius libero vel risus condimentum suscipit. Nullam tristique ultrices massa a volutpat. Donec sed dictum metus. Curabitur fringilla nibh eu ligula pharetra a interdum quam aliquam. Maecenas aliquam elit eu orci rutrum molestie. Proin nisl justo, varius a volutpat nec, ultricies sed sem. Nam sit amet imperdiet sem. Phasellus vitae mauris odio. Etiam in purus dui. Etiam ultricies, ante vel iaculis sodales, arcu leo adipiscing leo, sit amet mollis dui nisi non quam.</p>
      <p>Suspendisse sagittis laoreet dolor, vitae rhoncus arcu volutpat quis. Vestibulum at placerat dolor. Vivamus eu lacus ut enim molestie consectetur. Quisque ac lorem vel orci sagittis sollicitudin. Nunc ut quam sem, quis volutpat libero. Cum sociis natoque penatibus et magnis dis parturient montes, nascetur ridiculus mus. Vestibulum ante ipsum primis in faucibus orci luctus et ultrices posuere cubilia Curae; Donec tempor velit in velit feugiat sit amet vulputate nisl posuere..</p>
    </div>

    <div class="signatory">
      <p class="signatory__name"><b>JOHN</b> DOE</p>
      <p class="signatory__role">General director</p>
    </div>
    <div class="signature" role="img" aria-label="Handwritten signature of the general director"></div>

    <footer class="footer">
      <p class="footer__motto">A Legacy of Care</p>
      <div class="footer__rule"></div>
      <p class="footer__legal">Compliance disclosure: Securities and advisory services offered through QRT Financial.<br>Member NEXOB/DAFT.</p>
      <p class="footer__web">www.corlancewealth.example</p>
    </footer>
  </section>

  <section class="sheet sheet--follower">
    <div class="brand">
      <div class="brand__mark"></div>
      <div class="brand__name"><span class="brand__line1">Corlance</span><span class="brand__line2">Wealth Management</span></div>
    </div>

    <footer class="footer">
      <p class="footer__motto">A Legacy of Care</p>
      <div class="footer__rule"></div>
      <p class="footer__legal">Compliance disclosure: Securities and advisory services offered through QRT Financial.<br>Member NEXOB/DAFT.</p>
      <p class="footer__web">www.corlancewealth.example</p>
    </footer>
  </section>

  <svg class="badge" style="left:56px;top:48px" viewBox="0 0 70 62" aria-label="1">
    <polygon points="18,3 52,3 67,31 52,59 18,59 3,31" fill="var(--paper)" stroke="var(--badge)" stroke-width="4"/>
    <text x="35" y="41" text-anchor="middle">1</text>
  </svg>
  <svg class="badge" style="left:630px;top:48px" viewBox="0 0 70 62" aria-label="2">
    <polygon points="18,3 52,3 67,31 52,59 18,59 3,31" fill="var(--paper)" stroke="var(--badge)" stroke-width="4"/>
    <text x="35" y="41" text-anchor="middle">2</text>
  </svg>

</main>
</body>
</html>
```